Lanterns After Rain - CD cover indie music

This is my 4th and final album. I am sharing my story of trials, pain and persistence that led me here, like a sound track to a short film.
I would like a design that communicates both a painful phase of life, yet tranquility and beauty found as life winds down. Can be illustrated or photograph.
On front design should have title 'Lanterns After Rain' and artist name.
I will need to add credits and song list.
I am thinking a booklet will be added with lyrics and a few photos and plan to work with this artist. Thank you

Target Market(s)

Folk, easy listening, story telling

Industry/Entity Type

Indie music - independent

Font styles to use
Sans Serif
Other font styles liked:
• I like also verdana font.

Requirements
Nice to have
• a contrast of colors to emotions may work well. There is a portuguese word ‘saudade’ that expresses sadness, but longing also.
Should not have
• No bright red. Not busy. No images of people or animals.

```html
<!DOCTYPE html>
<html lang="en">
<head>
<meta charset="utf-8">
<title>Lanterns After Rain – Album Cover</title>
<link rel="stylesheet" href="https://fonts.googleapis.com/css2?family=Lobster&family=Raleway:wght@300;400&display=swap">
<style>
  :root {
    --page: #ffffff;
    --sun: #f7a43a;
    --sky: #5fa6a2;
    --car: #c7372a;
    --road: #2e3440;
    --road-line: #e8902a;
    --teal-brush: #6cc0bb;
    --title-shadow: #1f5a56;
    --ink-light: #f8f6f2;
    --badge: #000000;
  }
  * { margin: 0; padding: 0; box-sizing: border-box; }
  html, body {
    width: 1200px; height: 1199px; overflow: hidden;
    background: var(--page);
  }
  .cover {
    position: absolute; left: 113px; top: 94px;
    width: 974px; height: 973px; overflow: hidden;
    box-shadow: 0 22px 30px -12px rgba(0,0,0,.25);
  }
  .cover-photo {
    position: absolute; inset: 0;
    background:
      radial-gradient(ellipse 45% 40% at 18% 22%, rgba(255,220,140,.95), rgba(247,164,58,0) 70%),
      radial-gradient(ellipse 40% 55% at 85% 35%, var(--car), rgba(199,55,42,0) 75%),
      radial-gradient(ellipse 35% 40% at 55% 95%, var(--road-line), rgba(232,144,42,0) 75%),
      linear-gradient(180deg, var(--sun) 0%, var(--sky) 30%, #7a7a55 50%, #5b5f66 65%, var(--road) 100%);
  }
  .brush-band { position: absolute; inset: 0; width: 974px; height: 973px; }
  .artist-name {
    position: absolute; top: 62px; left: 0; width: 946px;
    text-align: center;
    font: 300 27px/1 "Raleway", sans-serif;
    letter-spacing: 0.55em; color: var(--ink-light);
  }
  .album-title {
    position: absolute; left: 120px; top: 300px; width: 640px;
    transform: rotate(-36deg); transform-origin: center;
    font-family: "Lobster", cursive; color: var(--ink-light);
    text-shadow: 4px 6px 0 var(--title-shadow);
    line-height: .95; text-align: center;
  }
  .album-title span { display: block; }
  .album-title .line-one { font-size: 132px; }
  .album-title .line-two { font-size: 118px; }
  .tagline {
    position: absolute; left: 238px; top: 900px;
    font: 400 17.5px/1 "Raleway", sans-serif;
    letter-spacing: .06em; color: var(--ink-light);
  }
  .edition-badge {
    position: absolute; left: 803px; top: 848px;
    width: 149px; height: 125px; background: var(--badge);
    color: var(--ink-light); text-align: center;
  }
  .edition-badge .number {
    display: block; margin-top: 10px;
    font: 60px/1 "Lobster", cursive; transform: rotate(-6deg);
  }
  .edition-badge .label {
    display: block; margin-top: 4px;
    font: 300 22px/1 "Raleway", sans-serif; letter-spacing: .18em;
  }
</style>
</head>
<body>
  <main class="cover">
    <div class="cover-photo" role="img" aria-label="Photograph of a red car on a mountain road at sunset, low angle over the asphalt and yellow centre line"></div>

    <svg class="brush-band" viewBox="0 0 974 973" aria-hidden="true">
      <polygon fill="var(--teal-brush)" opacity=".82"
        points="0,640 610,290 830,330 850,470 600,620 470,760 290,860 150,950 100,860 0,850"/>
    </svg>

    <p class="artist-name">ARTIST NAME</p>

    <h1 class="album-title">
      <span class="line-one">Lanterns</span>
      <span class="line-two">After Rain</span>
    </h1>

    <p class="tagline">MY STORY OF TRIALS, PAIN AND PERSISTENCE</p>

    <div class="edition-badge">
      <span class="number">4th</span>
      <span class="label">ALBUM</span>
    </div>
  </main>
</body>
</html>
```